Small Cosmetics Business needs a label design

We need a label design to affix on our cosmetic products made in Norfolk, England. The label needs to have the manufacturer's name, the product name, an ingredients list, an indication of use (ritual), contact details of manufacturer, weight, period after opening logo, batch number. We would like the label to highlight (in the form of sticker or tags) that the products are 100% natural, that they are hand made, that they do not contain preservatives or chemicals.Attached is a file with typical information for the label. The label should have colours, clarity and evoke nature, luxury.

Target Market(s)

UK

Industry/Entity Type

Cosmetics

Logo Text

Toril Sefa, Shape Grace

Font styles to use
Decorative

```html
<!DOCTYPE html>
<html lang="en">
<head>
<meta charset="utf-8">
<title>Toril Sefa – Palm Reverie Label</title>
<link rel="stylesheet" href="https://fonts.googleapis.com/css2?family=Great+Vibes&family=Dancing+Script:wght@700&family=Open+Sans:wght@400;600;700&display=swap">
<style>
  :root {
    --backdrop: #e4e5e6;
    --label-rim: #dfe4e6;
    --label-teal: #9fc6c6;
    --label-lime: #cbd96c;
    --brand-pink: #e0177f;
    --accent-yellow: #f3ec2a;
    --ink: #1d2a2a;
  }
  * { margin: 0; padding: 0; box-sizing: border-box; }
  html, body {
    width: 1200px;
    height: 1200px;
    overflow: hidden;
    background: var(--backdrop);
  }
  .label {
    position: absolute;
    left: 140px;
    top: 140px;
    width: 920px;
    height: 920px;
    border-radius: 50%;
    background: var(--label-rim);
    padding: 8px;
  }
  .label-pattern {
    width: 100%;
    height: 100%;
    border-radius: 50%;
    background:
      radial-gradient(circle at 30% 35%, rgba(203,217,108,0.75) 0%, rgba(203,217,108,0) 45%),
      radial-gradient(circle at 72% 60%, rgba(203,217,108,0.7) 0%, rgba(203,217,108,0) 42%),
      radial-gradient(circle at 50% 85%, rgba(203,217,108,0.55) 0%, rgba(203,217,108,0) 40%),
      var(--label-teal);
  }
  .brand-dot {
    position: absolute;
    left: 50%;
    top: 60px;
    width: 90px;
    height: 90px;
    margin-left: -45px;
    border-radius: 50%;
    background: #f4f1c9;
  }
  .brand-name {
    position: absolute;
    left: 0;
    right: 0;
    top: 160px;
    text-align: center;
    font-family: "Great Vibes", cursive;
    font-size: 96px;
    line-height: 1;
    color: var(--brand-pink);
  }
  .product-name {
    position: absolute;
    left: 0;
    right: 0;
    top: 290px;
    text-align: center;
    font-family: "Dancing Script", cursive;
    font-weight: 700;
    font-size: 124px;
    line-height: 1;
    color: var(--brand-pink);
    transform: rotate(-4deg);
    -webkit-text-stroke: 5px var(--accent-yellow);
    paint-order: stroke fill;
  }
  .product-info {
    position: absolute;
    left: 190px;
    width: 540px;
    top: 468px;
    text-align: center;
    font-family: "Open Sans", sans-serif;
    font-size: 15px;
    line-height: 21px;
    color: var(--ink);
  }
  .product-info p + p { margin-top: 8px; }
  .info-heading {
    font-weight: 700;
    color: var(--brand-pink);
  }
  .net-weight {
    position: absolute;
    left: 195px;
    width: 140px;
    top: 650px;
    text-align: center;
    font-family: "Open Sans", sans-serif;
    color: var(--ink);
  }
  .net-weight .weight-value {
    display: block;
    font-weight: 700;
    font-size: 34px;
    line-height: 1.1;
    color: var(--brand-pink);
  }
  .net-weight .weight-caption {
    font-size: 13px;
    font-weight: 600;
  }
  .shelf-details {
    position: absolute;
    left: 585px;
    width: 150px;
    top: 630px;
    text-align: center;
    font-family: "Open Sans", sans-serif;
    color: var(--ink);
  }
  .pao-icon { display: block; margin: 0 auto 4px; }
  .batch-number {
    font-size: 13px;
    font-weight: 600;
  }
  .maker-contact {
    position: absolute;
    left: 260px;
    width: 400px;
    top: 782px;
    text-align: center;
    font-family: "Open Sans", sans-serif;
    font-size: 13px;
    line-height: 18px;
    font-weight: 600;
    color: var(--ink);
  }
  .label-graphics {
    position: absolute;
    left: 0;
    top: 0;
    width: 920px;
    height: 920px;
    overflow: visible;
    pointer-events: none;
  }
  .claim-ring {
    font-family: "Open Sans", sans-serif;
    font-weight: 700;
    font-size: 19px;
    fill: var(--ink);
  }
  .badge-star {
    fill: var(--brand-pink);
    stroke: var(--accent-yellow);
    stroke-width: 4;
  }
  .badge-figure {
    font-family: "Open Sans", sans-serif;
    font-weight: 700;
    font-size: 50px;
    fill: var(--accent-yellow);
  }
  .badge-word {
    font-family: "Open Sans", sans-serif;
    font-weight: 700;
    font-size: 24px;
    fill: var(--accent-yellow);
  }
</style>
</head>
<body>
  <div class="label">
    <div class="label-pattern" role="img" aria-label="Teal background with lime green ornamental floral swirl pattern"></div>
    <div class="brand-dot"></div>
    <div class="brand-name">Toril Sefa</div>
    <div class="product-name">Palm Reverie</div>

    <div class="product-info">
      <p><span class="info-heading">Ingredients:</span> Cocos Nucifera (Coconut) Oil, Butyrospermum Parkii (Shea) Butter, Cera Alba, Tocopherol.</p>
      <p><span class="info-heading">Ritual:</span> Warm a little between your palms, massage slowly into damp skin and breathe deeply.</p>
    </div>

    <div class="net-weight">
      <span class="weight-value">100 g</span>
      <span class="weight-caption">Net Weight</span>
    </div>

    <div class="shelf-details">
      <svg class="pao-icon" width="54" height="50" viewBox="0 0 54 50" aria-label="Use within 12 months of opening">
        <path d="M8 14 L16 4 L40 4" fill="none" stroke="#1d2a2a" stroke-width="2.5" stroke-linejoin="round"/>
        <rect x="6" y="14" width="42" height="32" rx="3" fill="none" stroke="#1d2a2a" stroke-width="2.5"/>
        <text x="27" y="37" text-anchor="middle" font-family="Open Sans, sans-serif" font-weight="700" font-size="15" fill="#1d2a2a">12M</text>
      </svg>
      <span class="batch-number">Batch No. TS-0423</span>
    </div>

    <div class="maker-contact">
      Toril Sefa, Norwich, Norfolk, England<br>
      hello@torilsefa.co.uk · 01632 960 418
    </div>

    <svg class="label-graphics" viewBox="0 0 920 920" xmlns="http://www.w3.org/2000/svg">
      <defs>
        <path id="claim-arc" d="M 34 520 A 430 430 0 0 0 890 460"/>
      </defs>
      <text class="claim-ring">
        <textPath href="#claim-arc" textLength="1270" lengthAdjust="spacing">Handmade In Norfolk Handmade In Norfolk Contains No Preservatives And No Chemicals</textPath>
      </text>
      <g class="natural-badge" transform="translate(460 690) rotate(-15) scale(0.8)">
        <polygon class="badge-star" points="100,0 83,13.1 95.1,30.9 74.8,38.1 80.9,58.8 59.4,59.4 58.8,80.9 38.1,74.8 30.9,95.1 13.1,83 0,100 -13.1,83 -30.9,95.1 -38.1,74.8 -58.8,80.9 -59.4,59.4 -80.9,58.8 -74.8,38.1 -95.1,30.9 -83,13.1 -100,0 -83,-13.1 -95.1,-30.9 -74.8,-38.1 -80.9,-58.8 -59.4,-59.4 -58.8,-80.9 -38.1,-74.8 -30.9,-95.1 -13.1,-83 0,-100 13.1,-83 30.9,-95.1 38.1,-74.8 58.8,-80.9 59.4,-59.4 80.9,-58.8 74.8,-38.1 95.1,-30.9 83,-13.1"/>
        <text class="badge-figure" x="0" y="8" text-anchor="middle">100%</text>
        <text class="badge-word" x="0" y="38" text-anchor="middle">Natural</text>
      </g>
    </svg>
  </div>
</body>
</html>
```